Velbrook App Homepage Design making customers feel in control of their spend

Hi,
We need a App Homepage design with a UI similar to the attached mock up on an Quillo 4. The app is intended to put customers in control of their usage and spend on their fixed phone, broadband, mobile, gas and electricity.

Please fee free to propose improvements to the background images, icons, colours, etc.

Any questions please let me know.

Thanks
Tomasz

Target Market(s)

Consumer customers

Industry/Entity Type

Internet

Font styles to use
Sans Serif

Colors
3276b5
0255a3
85acd3
cfdeed
ffffff

Requirements
Must have
• Content in line with the guidelines in the attached mock up

```html
<!DOCTYPE html>
<html lang="en">
<head>
<meta charset="utf-8">
<title>Velbrook – Home</title>
<link href="https://fonts.googleapis.com/css2?family=Source+Sans+3:wght@300;400;600;700&display=swap" rel="stylesheet">
<style>
  :root {
    --bg: #000000;
    --white: #ffffff;
    --blue-mid: #3276b5;
    --blue-deep: #0255a3;
    --blue-soft: #85acd3;
    --blue-pale: #cfdeed;
    --brand-navy: #1b3a8c;
    --menu-grey: #8a8a8a;
    --label-dark: #111111;
    --amount: #e6edf6;
  }
  * { box-sizing: border-box; margin: 0; padding: 0; }
  html, body { width: 673px; height: 1200px; overflow: hidden; background: var(--bg); }
  body { font-family: "Source Sans 3", sans-serif; }

  .home-screen { position: relative; width: 673px; height: 1200px; background: var(--bg); }

  .menu-toggle { position: absolute; left: 24px; top: 22px; width: 53px; height: 40px;
    display: flex; flex-direction: column; justify-content: space-between; }
  .menu-toggle span { display: block; height: 7px; background: var(--menu-grey); border-radius: 2px; }

  .brand { position: absolute; left: 0; right: 0; top: 112px; display: flex;
    align-items: center; justify-content: center; gap: 24px; }
  .brand-dot { width: 104px; height: 104px; border-radius: 50%; background: var(--blue-mid); }
  .brand-name { font-size: 82px; font-weight: 600; color: var(--brand-navy); line-height: 1; letter-spacing: 1px; }

  .greeting { position: absolute; left: 0; right: 0; top: 240px; text-align: center;
    font-size: 30px; font-weight: 400; color: var(--blue-soft); }
  .welcome { position: absolute; left: 0; right: 0; top: 276px; text-align: center;
    font-size: 42px; font-weight: 400; color: var(--blue-soft); }

  .support-button { position: absolute; left: 88px; top: 359px; width: 510px; height: 66px;
    background: var(--white); border-radius: 18px; display: flex; align-items: center;
    justify-content: center; font-size: 30px; color: var(--blue-mid); text-decoration: none; }

  .spend-chart { position: absolute; left: 0; top: 0; width: 673px; height: 1200px; }
  .slice-label { font-family: "Source Sans 3", sans-serif; font-size: 23px; font-weight: 600;
    fill: var(--label-dark); text-anchor: middle; }

  .total-caption { position: absolute; left: 0; right: 0; top: 985px; text-align: center;
    font-size: 38px; font-weight: 300; color: var(--white); }
  .total-amount { position: absolute; left: 0; right: 0; top: 1030px; text-align: center;
    font-size: 38px; font-weight: 700; color: var(--amount); }

  .billing-summary { position: absolute; left: 88px; top: 1093px; width: 510px; height: 86px;
    background: var(--white); border-radius: 18px; display: flex; flex-direction: column;
    align-items: center; justify-content: center; font-size: 23px; line-height: 1.2; color: var(--blue-mid); }
</style>
</head>
<body>
<main class="home-screen">
  <div class="menu-toggle" aria-label="Menu"><span></span><span></span><span></span></div>

  <header class="brand">
    <div class="brand-dot"></div>
    <div class="brand-name">Velbrook</div>
  </header>

  <p class="greeting">Good Evening Marina !</p>
  <h1 class="welcome">Welcome to Velbrook</h1>

  <a class="support-button" href="#">Call 24 / 7 Support</a>

  <svg class="spend-chart" viewBox="0 0 673 1200" aria-label="Spend breakdown">
    <path d="M335 702 L335 490 A212 212 0 0 1 540.3 754.7 Z" fill="var(--blue-pale)"/>
    <path d="M335 702 L540.3 754.7 A212 212 0 0 1 459.6 873.5 Z" fill="var(--blue-soft)"/>
    <path d="M335 702 L459.6 873.5 A212 212 0 0 1 210.4 873.5 Z" fill="var(--blue-deep)"/>
    <path d="M335 702 L210.4 873.5 A212 212 0 0 1 126.8 662.3 Z" fill="var(--blue-mid)"/>
    <path d="M335 702 L126.8 662.3 A212 212 0 0 1 335 490 Z" fill="var(--white)"/>

    <text class="slice-label" x="449" y="626">Electricity</text>
    <text class="slice-label" x="449" y="656">(29%)</text>
    <text class="slice-label" x="452" y="800">Gas</text>
    <text class="slice-label" x="452" y="830">(11%)</text>
    <text class="slice-label" x="316" y="836">Mobile</text>
    <text class="slice-label" x="316" y="866">(20%)</text>
    <text class="slice-label" x="206" y="719">Calls</text>
    <text class="slice-label" x="206" y="749">(18%)</text>
    <text class="slice-label" x="236" y="591">Fibre</text>
    <text class="slice-label" x="236" y="621">(22%)</text>
  </svg>

  <p class="total-caption">Your current total charges</p>
  <p class="total-amount">$ 68.39</p>

  <section class="billing-summary">
    <span>Last Bill : $ 75.76 on 09 / 12 / 2016</span>
    <span>Allowance renews in 18 days</span>
  </section>
</main>
</body>
</html>
```